Business Card for Hollin Ledger - A cannabis publication for executives.

I'd like some business cards for Hollin Ledger. The logo is done (great job!) and I need a card design I will use with PELT. I made it a short project to allow time for printing before an event. These will be standard sized cards (final artwork size 3.66" x 2.16" at 300dpi) with a final card size of 3.5" x 2.0". (See PELT.example if you need more info.) I might try rounded corners but am not sure yet. I think the design will work okay with rounded.

Hollin Ledger will be a bi-weekly publication for the cannabis industry. It is targeted to investors and industry executives, not consumers or pot smokers. So our market is more B2B. However I am open to creativity and making the card something people remark on.

My contact for card:

Dara Venholm
Founder/CEO
dara@hollinledger.example

2746 Marrow Lane
Boston MA 02391
(617)555-0193

Target Market(s)

Executives, Industry people and investors in the Cannabis sector.

Contact Information for Business Card

PELT does do double sided and the second side can be the same or different images. Only one side is required but use of the second side would be a bonus.

Font styles to use
Serif
Sans Serif
Decorative

Colors

Designer to choose colors to be used in the design.

Requirements
Must have
• Logo, contact info
Nice to have
• Style and design to make the card stand out in a crowd.

```html
<!DOCTYPE html>
<html lang="en">
<head>
<meta charset="utf-8">
<title>Hollin Ledger — Business Card</title>
<link rel="stylesheet" href="https://fonts.googleapis.com/css2?family=Crimson+Pro:wght@400;600&display=swap">
<style>
  :root {
    --bg: #e2e2e2;
    --paper: #ffffff;
    --brand-blue: #1474bd;
    --brand-green: #82ad35;
    --ink: #2a2a2a;
  }
  * { box-sizing: border-box; margin: 0; padding: 0; }
  html, body { width: 1200px; height: 960px; overflow: hidden; }
  body {
    background: var(--bg);
    font-family: "Crimson Pro", Georgia, serif;
    position: relative;
  }
  .card {
    position: absolute;
    left: 250px;
    width: 700px;
    height: 400px;
    border-radius: 26px;
    overflow: hidden;
    box-shadow: 0 4px 14px rgba(0,0,0,0.12);
  }
  .card--front { top: 60px; background: var(--paper); }
  .card--back  { top: 500px; background: var(--brand-green); }

  .brand { position: absolute; display: flex; align-items: center; gap: 16px; }
  .brand__dot { border-radius: 50%; flex: none; }
  .brand__name { font-weight: 400; line-height: 1; white-space: nowrap; }

  .card--front .brand { left: 230px; top: 48px; }
  .card--front .brand__dot { width: 34px; height: 34px; background: var(--brand-green); }
  .card--front .brand__name { font-size: 46px; color: var(--brand-blue); }

  .contact__name {
    position: absolute; left: 52px; top: 140px;
    font-size: 32px; font-weight: 600; letter-spacing: 0.5px;
    color: var(--brand-blue); text-transform: uppercase;
  }
  .contact__role {
    position: absolute; left: 54px; top: 180px;
    font-size: 24px; color: var(--brand-green);
  }
  .contact__address {
    position: absolute; left: 250px; top: 232px;
    font-size: 18px; color: var(--ink);
  }
  .contact__phone {
    position: absolute; left: 150px; top: 262px;
    width: 300px; height: 46px;
    background: var(--brand-blue);
    clip-path: polygon(0 0, 100% 0, 100% 100%, 92% 100%, 0 100%);
    color: #fff; font-size: 30px; line-height: 46px; padding-left: 18px;
  }
  .contact__phone::after { content: none; }
  .contact__email {
    position: absolute; left: 150px; top: 322px;
    font-size: 19px; color: var(--ink);
  }
  .dots { position: absolute; right: 0; top: 0; width: 170px; height: 400px; }

  .card--back .brand { left: 50%; top: 50%; transform: translate(-50%, -50%); }
  .card--back .brand__dot { width: 52px; height: 52px; background: #fff; }
  .card--back .brand__name { font-size: 72px; color: #fff; }
</style>
</head>
<body>
  <section class="card card--front" aria-label="Card front">
    <div class="brand">
      <span class="brand__dot"></span>
      <span class="brand__name">Hollin Ledger</span>
    </div>
    <p class="contact__name">Dara Venholm</p>
    <p class="contact__role">Founder/CEO</p>
    <p class="contact__address">2746 Marrow Lane Boston MA 02391</p>
    <p class="contact__phone">(617) 555 0193</p>
    <p class="contact__email">dara@hollinledger.example</p>
    <svg class="dots" viewBox="0 0 170 400" aria-hidden="true">
      <g fill="var(--brand-blue)">
        <circle cx="150" cy="18" r="10"/>
        <circle cx="120" cy="110" r="10"/>
        <circle cx="100" cy="190" r="10"/>
        <circle cx="80" cy="270" r="10"/>
        <circle cx="60" cy="350" r="10"/>
      </g>
      <g fill="var(--brand-green)">
        <circle cx="150" cy="60" r="10"/>
        <circle cx="150" cy="100" r="10"/>
        <circle cx="130" cy="170" r="10"/>
        <circle cx="150" cy="220" r="10"/>
        <circle cx="110" cy="250" r="10"/>
        <circle cx="130" cy="300" r="10"/>
        <circle cx="150" cy="340" r="10"/>
        <circle cx="110" cy="385" r="10"/>
      </g>
      <circle cx="20" cy="392" r="9" fill="var(--brand-blue)"/>
    </svg>
  </section>

  <section class="card card--back" aria-label="Card back">
    <div class="brand">
      <span class="brand__dot"></span>
      <span class="brand__name">Hollin Ledger</span>
    </div>
  </section>
</body>
</html>
```